PulseLedgerPro.Com PowerPoint

I need a PowerPoint layout for my presentations. My business is called PulseLedgerPro.Com - my presentations teach cardiologists how to document their procedures and visits and teaches them how to bill accurately for them.

Industry/Entity Type

Business

Requirements
Must have
• the logo should be subtly there on each page - perhaps as a watermark? I'm really not creative; please help.

```html
<!DOCTYPE html>
<html lang="en">
<head>
<meta charset="utf-8">
<title>PulseLedgerPro.Com – Presentation Template</title>
<link href="https://fonts.googleapis.com/css2?family=Open+Sans:wght@400;600;700&display=swap" rel="stylesheet">
<style>
  :root{
    --page:#ffffff;
    --brand-red:#a20a10;
    --accent-red:#c3141d;
    --bright-red:#e5434b;
    --deep-red:#860d13;
    --band-dark:#2e2e2e;
    --title-grey:#5e5e5e;
    --body-grey:#606060;
    --light-grey:#9a9a9a;
    --row-a:#f1d2d3;
    --row-b:#f8e7e7;
    --photo-blue:#c9d6da;
    --photo-light:#dfe6e4;
    --photo-red:#b8252a;
  }
  *{box-sizing:border-box;margin:0;padding:0}
  html,body{width:1200px;height:900px;overflow:hidden;background:var(--page)}
  body{position:relative;font-family:"Open Sans",Arial,sans-serif;color:var(--body-grey)}

  .slide{position:absolute;width:378px;height:284px;background:#fff;
    box-shadow:0 1px 4px rgba(0,0,0,.45);overflow:hidden}
  .col-1{left:17px}.col-2{left:409px}.col-3{left:801px}
  .row-1{top:10px}.row-2{top:307px}.row-3{top:604px}

  /* cover */
  .photo{position:absolute}
  .photo-desk{left:4px;top:4px;width:94px;height:148px;
    background:linear-gradient(160deg,#e9eef0 0%,var(--photo-blue) 55%,#5b6770 100%)}
  .photo-cells{left:102px;top:4px;width:126px;height:148px;
    background:radial-gradient(circle at 40% 40%,#d9453f 0%,var(--photo-red) 50%,#7a1013 100%)}
  .photo-doctor{left:232px;top:4px;width:142px;height:148px;
    background:linear-gradient(120deg,#b9cfcf 0%,var(--photo-light) 50%,#f4f6f5 100%)}
  .cover-band{position:absolute;left:4px;top:156px;width:370px;height:94px;background:var(--band-dark)}
  .cover-title{position:absolute;left:12px;top:30px;font-size:12.5px;color:#fff}
  .cover-sub{position:absolute;left:12px;top:58px;font-size:9.5px;color:var(--light-grey)}
  .cover-band.closing{text-align:center}
  .closing .cover-title{left:0;right:0;top:30px;font-size:14px}
  .closing .cover-sub{left:0;right:0;top:60px;font-size:9.5px}
  .cover-logo{position:absolute;left:4px;top:253px;width:94px;height:27px;display:flex;align-items:center;gap:3px;padding-left:3px}
  .cover-footer{position:absolute;left:102px;top:253px;width:272px;height:27px;background:var(--brand-red);
    color:#fff;font-size:6px;display:flex;align-items:center;padding:0 8px}

  .brand-mark{width:6px;height:6px;background:var(--brand-red);flex:none}
  .brand-name{font-size:7px;font-weight:700;color:var(--brand-red);white-space:nowrap}

  /* content slides */
  .title-bar{position:absolute;left:4px;top:4px;width:302px;height:44px;background:var(--title-grey);
    color:#fff;font-size:14.5px;padding:14px 0 0 8px}
  .thumb{position:absolute;left:310px;top:4px;width:64px;height:44px;
    background:linear-gradient(120deg,#b9cfcf,#eef2f0)}
  .footer{position:absolute;left:4px;top:262px;width:294px;height:17px;background:var(--brand-red);
    color:#fff;font-size:5.5px;display:flex;align-items:center;padding:0 8px}
  .footer-logo{position:absolute;left:300px;top:262px;width:76px;height:17px;display:flex;align-items:center;gap:2px}
  .footer-logo .brand-name{font-size:6.4px}
  .date{width:100px}
  .pres-name{flex:1}
  .page-num{width:12px;text-align:right}

  .body{position:absolute;left:10px;top:56px;right:10px}
  .lvl1{position:relative;padding-left:13px;font-size:9.4px;line-height:1.27;margin-bottom:4px;color:var(--body-grey)}
  .lvl1::before{content:"";position:absolute;left:2px;top:3px;width:6px;height:6px;border:1.2px solid var(--accent-red);border-radius:1px 1px 4px 4px}
  .lvl2{position:relative;padding-left:26px;font-size:8px;line-height:1.4;margin-bottom:5px;color:var(--body-grey)}
  .lvl2::before{content:"–";position:absolute;left:14px;top:0;color:var(--accent-red)}
  .narrow{width:185px}

  .side-photo{position:absolute;left:207px;top:62px;width:160px;height:104px;border-radius:8px;
    background:linear-gradient(150deg,#cfd9dc 0%,#eef2f2 55%,#c2d0d4 100%)}
  .side-reflection{position:absolute;left:207px;top:168px;width:160px;height:28px;
    background:linear-gradient(#e6ebec,rgba(255,255,255,0));opacity:.6}

  .topic{position:absolute;top:56px;width:170px}
  .topic-a{left:10px}.topic-b{left:194px}
  .topic-head{font-size:10px;font-weight:700;color:var(--accent-red);margin:4px 0 6px}
  .topic .lvl1{color:var(--accent-red)}
  .divider{position:absolute;left:189px;top:56px;height:186px;border-left:1px dashed var(--bright-red)}

  .chart-box{position:absolute;left:192px;top:52px;width:182px;height:206px;border:1px dashed var(--bright-red)}
  .chart-split{position:absolute;left:0;right:0;top:104px;border-top:1px dashed var(--bright-red)}
  .chart-box svg{position:absolute;left:0;display:block}

  .table-title{position:absolute;left:0;right:0;top:78px;text-align:center;font-size:11px;font-weight:700;color:var(--accent-red)}
  .data-table{position:absolute;left:58px;top:116px;border-collapse:collapse;font-size:7.6px}
  .data-table th{background:var(--accent-red);color:#fff;font-weight:700;padding:3px 4px;border:1px solid #fff;width:54px}
  .data-table td{padding:2.5px 4px;text-align:center;border:1px solid #fff;color:#333}
  .data-table tr:nth-child(odd) td{background:var(--row-a)}
  .data-table tr:nth-child(even) td{background:var(--row-b)}
</style>
</head>
<body>

<!-- 1 cover -->
<section class="slide col-1 row-1">
  <div class="photo photo-desk" role="img" aria-label="Hands filling in a form on a clipboard beside a keyboard"></div>
  <div class="photo photo-cells" role="img" aria-label="Red blood cells floating"></div>
  <div class="photo photo-doctor" role="img" aria-label="Doctor's arm holding a stethoscope in a clinic"></div>
  <div class="cover-band">
    <p class="cover-title">Lorem ipsum dolor sit amet, consectetur adipiscing elit</p>
    <p class="cover-sub">Duis molestie, mi id consequat convallis</p>
  </div>
  <div class="cover-logo"><span class="brand-mark"></span><span class="brand-name">PulseLedgerPro.Com</span></div>
  <div class="cover-footer"><span class="date">28-12-2013</span><span class="pres-name">Presentation Name</span><span class="page-num">1</span></div>
</section>

<!-- 2 text -->
<section class="slide col-2 row-1">
  <div class="title-bar">Text slide</div>
  <div class="thumb" role="img" aria-label="Doctor with stethoscope"></div>
  <div class="body">
    <p class="lvl1">Lorem ipsum dolor sit amet, consectetur adipiscing elit.</p>
    <p class="lvl2">Duis faucibus nunc eu felis laoreet viverra. Vestibulum ipsum quam, ultricies id fringilla eget,</p>
    <p class="lvl2">Nam elementum ut nisl quis viverra. Morbi dignissim metus quis lacus adipiscing, at mattis dolor feugiat. Proin ut lorem sollicitudin, facilisis lacus vitae.</p>
    <p class="lvl1">Vivamus nec augue elementum, porta leo eu, auctor turpis. Fusce suscipit enim vitae nibh varius tincidunt. Aenean vel leo sem.</p>
    <p class="lvl1">Morbi a egestas ipsum. Donec ut lacus tincidunt, imperdiet sapien id, pharetra felis. Donec id sollicitudin enim.</p>
    <p class="lvl2">Sed bibendum eros a porta lobortis. Sed justo ante, ullamcorper et felis id, dictum aliquet eros. Vivamus ligula dolor, bibendum sit amet placerat vitae, condimentum ac ante.</p>
  </div>
  <div class="footer"><span class="date">28-12-2013</span><span class="pres-name">Presentation Name</span><span class="page-num">2</span></div>
  <div class="footer-logo"><span class="brand-mark"></span><span class="brand-name">PulseLedgerPro.Com</span></div>
</section>

<!-- 3 text and picture -->
<section class="slide col-3 row-1">
  <div class="title-bar">Text and picture slide</div>
  <div class="thumb" role="img" aria-label="Doctor with stethoscope"></div>
  <div class="body narrow">
    <p class="lvl1">Lorem ipsum dolor sit amet, consectetur adipiscing elit.</p>
    <p class="lvl2">Duis faucibus nunc eu felis laoreet viverra. Vestibulum ipsum quam, ultricies id fringilla eget,</p>
    <p class="lvl2">Nam elementum ut nisl quis viverra. Morbi dignissim metus quis lacus adipiscing, at mattis dolor feugiat. Proin ut lorem sollicitudin, facilisis lacus vitae.</p>
    <p class="lvl1">Vivamus nec augue elementum, porta leo eu, auctor turpis.</p>
    <p class="lvl2">Sed bibendum eros a porta lobortis.</p>
  </div>
  <div class="side-photo" role="img" aria-label="Clinician writing notes on a clipboard beside a blood pressure monitor"></div>
  <div class="side-reflection"></div>
  <div class="footer"><span class="date">28-12-2013</span><span class="pres-name">Presentation Name</span><span class="page-num">3</span></div>
  <div class="footer-logo"><span class="brand-mark"></span><span class="brand-name">PulseLedgerPro.Com</span></div>
</section>

<!-- 4 comparison -->
<section class="slide col-1 row-2">
  <div class="title-bar">Comparison Slide</div>
  <div class="thumb" role="img" aria-label="Doctor with stethoscope"></div>
  <div class="topic topic-a">
    <p class="topic-head">Topic A</p>
    <p class="lvl1">Lorem ipsum dolor sit amet, consectetur adipiscing elit</p>
    <p class="lvl2">Donec ut lacus tincidunt, imperdiet sapien id, pharetra felis.</p>
    <p class="lvl2">Donec id sollicitudin enim. Sed bibendum eros a porta lobortis.</p>
    <p class="lvl2">Sed justo ante, ullamcorper et felis id, dictum aliquet eros.</p>
  </div>
  <div class="divider"></div>
  <div class="topic topic-b">
    <p class="topic-head">Topic B</p>
    <p class="lvl1">Lorem ipsum dolor sit amet, consectetur adipiscing elit</p>
    <p class="lvl2">Donec ut lacus tincidunt, imperdiet sapien id, pharetra felis.</p>
    <p class="lvl2">Donec id sollicitudin enim. Sed bibendum eros a porta lobortis.</p>
    <p class="lvl2">Sed justo ante, ullamcorper et felis id, dictum aliquet eros.</p>
  </div>
  <div class="footer"><span class="date">28-12-2013</span><span class="pres-name">Presentation Name</span><span class="page-num">4</span></div>
  <div class="footer-logo"><span class="brand-mark"></span><span class="brand-name">PulseLedgerPro.Com</span></div>
</section>

<!-- 5 text and chart -->
<section class="slide col-2 row-2">
  <div class="title-bar">Text and chart slide</div>
  <div class="thumb" role="img" aria-label="Doctor with stethoscope"></div>
  <div class="body narrow">
    <p class="lvl1">Lorem ipsum dolor sit amet, consectetur adipiscing elit.</p>
    <p class="lvl2">Duis faucibus nunc eu felis laot viverra.</p>
    <p class="lvl2">Vestibulum ipsum quam, ultricies id fringilla eget,</p>
    <p class="lvl2">Nam elementum ut nisl quis viverra.</p>
    <p class="lvl1">Vivamus nec augue elementum, porta leo eu, auctor turpis.</p>
    <p class="lvl1">Morbi a egestas ipsum.</p>
    <p class="lvl2">Sed bibendum eros a porta lobortis.</p>
  </div>
  <div class="chart-box">
    <svg class="bar-chart" width="180" height="104" viewBox="0 0 180 104" style="top:0" font-family="Open Sans, sans-serif" font-size="5.5" fill="#333">
      <line x1="6" y1="88" x2="174" y2="88" stroke="#ccc" stroke-width=".6"/>
      <!-- scale: 13px per unit, baseline 88 -->
      <g>
        <rect x="18" y="32.1" width="8" height="55.9" fill="#e5434b"/>
        <rect x="26" y="56.8" width="8" height="31.2" fill="#c3141d"/>
        <rect x="34" y="62" width="8" height="26" fill="#860d13"/>
        <text x="19" y="29">4,3</text><text x="27" y="54">2,4</text><text x="36" y="59">2</text>
        <text x="16" y="97">Category 1</text>
      </g>
      <g>
        <rect x="58" y="55.5" width="8" height="32.5" fill="#e5434b"/>
        <rect x="66" y="30.8" width="8" height="57.2" fill="#c3141d"/>
        <rect x="74" y="62" width="8" height="26" fill="#860d13"/>
        <text x="58" y="52">2,5</text><text x="66" y="28">4,4</text><text x="76" y="59">2</text>
        <text x="56" y="97">Category 2</text>
      </g>
      <g>
        <rect x="98" y="42.5" width="8" height="45.5" fill="#e5434b"/>
        <rect x="106" y="64.6" width="8" height="23.4" fill="#c3141d"/>
        <rect x="114" y="49" width="8" height="39" fill="#860d13"/>
        <text x="98" y="39">3,5</text><text x="106" y="62">1,8</text><text x="116" y="46">3</text>
        <text x="96" y="97">Category 3</text>
      </g>
      <g>
        <rect x="138" y="29.5" width="8" height="58.5" fill="#e5434b"/>
        <rect x="146" y="51.6" width="8" height="36.4" fill="#c3141d"/>
        <rect x="154" y="23" width="8" height="65" fill="#860d13"/>
        <text x="138" y="27">4,5</text><text x="146" y="49">2,8</text><text x="156" y="20">5</text>
        <text x="136" y="97">Category 4</text>
      </g>
    </svg>
    <div class="chart-split"></div>
    <svg class="donut-chart" width="180" height="100" viewBox="0 0 180 100" style="top:106px" font-family="Open Sans, sans-serif" font-size="5.5">
      <text x="90" y="9" text-anchor="middle" fill="#333" font-size="6">Chart Title</text>
      <g transform="rotate(-90 92 56)" fill="none" stroke-width="17">
        <circle cx="92" cy="56" r="25" stroke="#c3141d" stroke-dasharray="92 157.1"/>
        <circle cx="92" cy="56" r="25" stroke="#e5434b" stroke-dasharray="35.9 157.1" stroke-dashoffset="-92"/>
        <circle cx="92" cy="56" r="25" stroke="#860d13" stroke-dasharray="15.7 157.1" stroke-dashoffset="-127.9"/>
        <circle cx="92" cy="56" r="25" stroke="#a8a8a8" stroke-dasharray="13.5 157.1" stroke-dashoffset="-143.6"/>
      </g>
      <text x="114" y="70" fill="#fff">8,2</text>
      <text x="57" y="66" fill="#fff">3,2</text>
      <text x="65" y="39" fill="#fff">1,4</text>
      <text x="80" y="32" fill="#fff">1,2</text>
    </svg>
  </div>
  <div class="footer"><span class="date">28-12-2013</span><span class="pres-name">Presentation Name</span><span class="page-num">5</span></div>
  <div class="footer-logo"><span class="brand-mark"></span><span class="brand-name">PulseLedgerPro.Com</span></div>
</section>

<!-- 6 table -->
<section class="slide col-3 row-2">
  <div class="title-bar">Table slide</div>
  <div class="thumb" role="img" aria-label="Doctor with stethoscope"></div>
  <p class="table-title">Table title</p>
  <table class="data-table">
    <tr><th>Category A</th><th>Category B</th><th>Category C</th><th>Category D</th><th>Category E</th></tr>
    <tr><td>111.222</td><td>444.000</td><td>777.222</td><td>666.111</td><td>333.222</td></tr>
    <tr><td>333.888</td><td>111.222</td><td>555.777</td><td>888.999</td><td>222.000</td></tr>
    <tr><td>555.333</td><td>666.777</td><td>111.222</td><td>999.222</td><td>888.555</td></tr>
    <tr><td>888.444</td><td>999.555</td><td>333.444</td><td>111.222</td><td>111.999</td></tr>
  </table>
  <div class="footer"><span class="date">28-12-2013</span><span class="pres-name">Presentation Name</span><span class="page-num">6</span></div>
  <div class="footer-logo"><span class="brand-mark"></span><span class="brand-name">PulseLedgerPro.Com</span></div>
</section>

<!-- 7 closing -->
<section class="slide col-1 row-3">
  <div class="photo photo-desk" role="img" aria-label="Hands filling in a form on a clipboard beside a keyboard"></div>
  <div class="photo photo-cells" role="img" aria-label="Red blood cells floating"></div>
  <div class="photo photo-doctor" role="img" aria-label="Doctor's arm holding a stethoscope in a clinic"></div>
  <div class="cover-band closing">
    <p class="cover-title">THANK YOU</p>
    <p class="cover-sub">FOR YOUR TIME</p>
  </div>
  <div class="cover-logo"><span class="brand-mark"></span><span class="brand-name">PulseLedgerPro.Com</span></div>
  <div class="cover-footer"><span class="date">28-12-2013</span><span class="pres-name">Presentation Name</span><span class="page-num">7</span></div>
</section>

</body>
</html>
```